Etiketten Fine-Tuning für Creatine Supplement
Zielgruppe
Bitte auf www.kelvora-vital.example hereinschauen.
Please check our webpage: www.kelvora-vital.example
Aufgabenstellung
Eine Vorlage besteht sowie ein Design Guide.
Das bestehende Etikett soll den letzten Feinschliff bekommen um den Kunden optisch zum Kauf anzuregen.
Das Design soll eindeutlich wiedererkennbar sein, große Änderungen sind nicht nötig. Ein minimalistischer Ansatz kann auch gewählt werden.
Weitere Produkte findet ihr auf der Homepage oder auf Zolvex unter dem Begriff Kelvora Vital.
Das Format sollte im Photoshop sein oder irgendwie dort editierbar sein da ich kein Illustrator habe.
Das Etikett muss einen 2 mm Rand für den Zuschnitt haben. Minimale Schriftgrösse ist 1.2mm
Etikettengrösse: 75 x210mm
Die Texte sind verbindlich und müssen verbleiben.
Alle Fonts sind in den Dateien.
A template exists as well as a design guide.
The existing label is to be given the final touches in order to visually encourage the customer to buy.
The design should be clearly recognizable, large changes are not necessary. A minimalist approach can also be chosen.
You can find more products on the homepage or on Zolvex under the term Kelvora Vital.
The format must be in Photoshop. The label must have a 2 mm margin for cutting.
Label size: 75 x210mm
The texts are legally binding and must remain so.

```html
<!DOCTYPE html>
<html lang="de">
<head>
<meta charset="utf-8">
<title>Kelvora Creatine+ Etikett</title>
<link rel="stylesheet" href="https://fonts.googleapis.com/css2?family=Montserrat:wght@200;800&family=Quicksand:wght@400;500;700&display=swap">
<style>
  :root {
    --canvas: #ffffff;
    --green-deep: #7fbf3a;
    --green-mid: #8dc73f;
    --green-light: #a6d25f;
    --white: #ffffff;
    --text-green: #8cc63f;
    --badge-dark: #1f1f1f;
  }
  html, body {
    margin: 0;
    width: 1200px;
    height: 1200px;
    overflow: hidden;
    background: var(--canvas);
  }
  .label {
    position: absolute;
    left: 100px;
    top: 270px;
    width: 1000px;
    height: 660px;
    background: linear-gradient(135deg, var(--green-deep) 0%, var(--green-mid) 45%, var(--green-light) 100%);
    color: var(--white);
    font-family: "Quicksand", sans-serif;
  }
  .front {
    position: absolute;
    left: 210px;
    top: 0;
    width: 580px;
    height: 100%;
  }
  .product-name {
    position: absolute;
    left: 60px;
    top: 52px;
    margin: 0;
    font-family: "Montserrat", sans-serif;
    font-weight: 800;
    font-size: 82px;
    line-height: 1;
    letter-spacing: -1px;
  }
  .product-sub {
    position: absolute;
    left: 58px;
    top: 142px;
    margin: 0;
    font-family: "Montserrat", sans-serif;
    font-weight: 200;
    font-size: 72px;
    line-height: 1;
    letter-spacing: -1px;
  }
  .brand {
    position: absolute;
    left: 0;
    width: 100%;
    top: 270px;
    display: flex;
    align-items: center;
    justify-content: center;
    gap: 14px;
    font-weight: 700;
    font-size: 30px;
  }
  .brand-dot {
    width: 30px;
    height: 30px;
    border: 5px solid var(--white);
    border-radius: 50%;
    box-sizing: border-box;
  }
  .rule {
    position: absolute;
    left: 0;
    width: 100%;
    height: 2px;
    background: var(--white);
  }
  .rule-top { top: 402px; }
  .rule-bottom { top: 540px; }
  .category {
    position: absolute;
    left: 52px;
    top: 404px;
    width: 446px;
    height: 34px;
    background: var(--white);
    color: var(--text-green);
    font-weight: 700;
    font-size: 22px;
    line-height: 34px;
    text-align: center;
  }
  .ingredients {
    position: absolute;
    left: 50px;
    top: 448px;
    margin: 0;
    font-weight: 500;
    font-size: 31px;
    line-height: 40px;
    letter-spacing: 0.3px;
  }
  .contents {
    position: absolute;
    left: 18px;
    top: 564px;
    display: flex;
    gap: 12px;
    align-items: center;
  }
  .capsule {
    width: 10px;
    height: 52px;
    border-radius: 5px;
    background: var(--white);
  }
  .contents p {
    margin: 0;
    font-size: 22px;
    line-height: 28px;
    font-weight: 400;
  }
  .contents b { font-weight: 700; }
  .divider {
    position: absolute;
    left: 270px;
    top: 542px;
    width: 2px;
    height: 98px;
    background: var(--white);
  }
  .badges {
    position: absolute;
    left: 292px;
    top: 554px;
  }
</style>
</head>
<body>
  <div class="label">
    <div class="front">
      <h1 class="product-name">KELVORA</h1>
      <p class="product-sub">CREATINE+</p>

      <div class="brand">
        <span class="brand-dot"></span>
        <span>Kelvora Vital</span>
      </div>

      <div class="rule rule-top"></div>
      <div class="category">Nahrungsergänzungsmittel</div>
      <p class="ingredients">Mit Creatine Monohydrate,<br>Beta-Alanin und D-Ribose</p>
      <div class="rule rule-bottom"></div>

      <div class="contents">
        <span class="capsule"></span>
        <p><b>150</b> Kapseln<br><b>30</b> Tagesportionen</p>
      </div>

      <div class="divider"></div>

      <svg class="badges" width="240" height="76" viewBox="0 0 240 76" aria-hidden="true">
        <polygon fill="var(--white)" points="38,2 46,10 57,7 60,18 71,21 68,32 76,38 68,44 71,55 60,58 57,69 46,66 38,74 30,66 19,69 16,58 5,55 8,44 0,38 8,32 5,21 16,18 19,7 30,10"/>
        <polygon fill="var(--white)" points="127,2 158,20 158,56 127,74 96,56 96,20"/>
        <rect x="170" y="4" width="58" height="68" rx="26" fill="var(--white)" opacity="0.85"/>
      </svg>
    </div>
  </div>
</body>
</html>
```